bold, classy, clean design for legal stationary and business cards - more modern than traditional
New law office stationary, that looks like the firm is bold, successful, professional, and not new.
bold, classy, clean design for legal stationary and business cards - more modern than traditional - Law
Creative Brief
Professional
Nora T. Pask
Law Office of Nora T. Pask, LLC 47 W. Orrin Avenue, Suite 315 Chicago, IL 60614
Office - 312-555-0148
Mobile - 773-555-0172
ntp@norapasklegal.example
www.norapasklegal.example
I have purchased a logo, and I hope that I attach the correct format. I am a new company, so I am trying to be cost conscious, yet have the card look like a million bucks. The logo is red and dark grey. I would like to keep the card to just those colors, and only have red on the front, I hope that saves money. If you think the type should be black rather than dark grey, I am OK with that. The back side (I think) should just be black or dark grey. I would like something professional and bold.
I would like these four areas of practice on the back of the card: personal injury wrongful death medical malpractice auto accidents perhaps putting a dash/diamond/line in-between the words
corasolmlegal corasolmlegal
Can you please show me stationary designs for letterhead and envelopes.

```html
<!DOCTYPE html>
<html lang="en">
<head>
<meta charset="utf-8">
<title>Nora T. Pask – Stationery Suite</title>
<link href="https://fonts.googleapis.com/css2?family=Cinzel:wght@400;600&family=Lato:wght@400;700&display=swap" rel="stylesheet">
<style>
  :root{
    --backdrop:#a7a7a7;
    --paper:#ffffff;
    --red:#c8202f;
    --charcoal:#565656;
    --flap:#3e3e3e;
    --ink:#1e1e1e;
    --grey:#6d6d6d;
    --rule:#9a9a9a;
  }
  *{box-sizing:border-box;margin:0;padding:0}
  html,body{width:1200px;height:673px;overflow:hidden;background:var(--backdrop)}
  .board{position:relative;width:1200px;height:673px;font-family:"Lato",Arial,sans-serif;color:var(--ink)}
  .piece{position:absolute;background:var(--paper);box-shadow:0 1px 3px rgba(0,0,0,.25)}

  /* logo lockup: plain square + name set in one colour and weight */
  .lockup{position:absolute;display:flex;align-items:center}
  .lockup .square{background:var(--red);flex:none}
  .lockup .divider{width:1px;background:var(--rule);align-self:stretch;margin:0 5px}
  .lockup .wordmark{font-family:"Cinzel",Georgia,serif;font-weight:400;color:var(--red);line-height:1.05}
  .lockup .wordmark .small{display:block;letter-spacing:.28em}
  .lockup .wordmark .big{display:block}
  .lockup.reverse .square{background:none;border:1.5px solid #fff}
  .lockup.reverse .wordmark{color:#fff}
  .lockup.reverse .divider{background:#bbb}

  .address{position:absolute;font-family:"Cinzel",Georgia,serif;color:var(--ink);line-height:1.35}

  /* business card back */
  .card-back{left:138px;top:72px;width:160px;height:91px;background:#fff;padding:4px}
  .card-back .field{position:relative;width:100%;height:100%;background:var(--charcoal);outline:1px solid #fff;outline-offset:-3px}
  .card-back .practice{position:absolute;left:55px;top:57px;width:55px;border:1px solid #ddd;
    font-family:"Lato",sans-serif;font-size:3.6px;color:#fff;text-align:center;line-height:1.25;padding:1px 0;text-transform:uppercase}

  /* business card front */
  .card-front{left:314px;top:72px;width:151px;height:91px}
  .card-front .holder{position:absolute;left:20px;top:56px;font-family:"Cinzel",serif;font-size:7.5px}
  .card-front .contacts{position:absolute;left:74px;top:56px;font-family:"Cinzel",serif;font-size:4.3px;line-height:1.5}
  .contacts .icon{display:inline-block;width:4px;height:4px;border-radius:50%;background:var(--red);margin-right:3px;vertical-align:middle}

  /* letterhead */
  .letterhead{left:492px;top:72px;width:383px;height:542px}
  .letter{position:absolute;left:61px;top:122px;width:285px;font-size:6.3px;line-height:1.55;font-weight:700}
  .letter .recipient{font-weight:400;font-size:5.6px;line-height:1.6;margin-bottom:14px}
  .letter .recipient strong{font-size:6.3px}
  .letter p{text-align:justify;margin-bottom:9px}
  .letter .closing{text-align:right;font-size:5.4px;margin:0}
  .signature{position:absolute;left:264px;top:432px;width:60px;height:42px;background:linear-gradient(135deg,#f1f1f1,#e4e4e4)}
  .letter-footer{position:absolute;left:0;right:0;top:514px;border-top:1px solid var(--rule);
    display:flex;justify-content:center;gap:36px;padding-top:6px;font-family:"Cinzel",serif;font-size:5.4px}

  /* envelopes */
  .envelope{left:88px;top:185px;width:386px;height:197px}
  .envelope-back{left:89px;top:403px;width:383px;height:196px;background:linear-gradient(180deg,#fdfdfd,#ececec)}
  .envelope-back svg{position:absolute;left:0;top:0}

  /* sheets */
  .second-sheet{left:892px;top:72px;width:188px;height:325px}
  .folder{left:956px;top:288px;width:195px;height:326px}
  .folder .practice{position:absolute;left:34px;top:136px;width:127px;height:57px;border:2px solid var(--grey);
    display:flex;flex-direction:column;justify-content:center;text-align:center;
    font-family:"Cinzel",serif;font-size:8.6px;line-height:1.25;color:var(--grey)}
</style>
</head>
<body>
<div class="board">

  <!-- Business card, back -->
  <section class="piece card-back">
    <div class="field">
      <div class="lockup reverse" style="left:30px;top:18px;height:18px">
        <span class="square" style="width:18px;height:18px"></span>
        <span class="divider"></span>
        <span class="wordmark"><span class="small" style="font-size:4.3px">Law Office of</span><span class="big" style="font-size:9px">Nora T. Pask</span></span>
      </div>
      <div class="practice">Personal Injury<br>Wrongful Death<br>Medical Malpractice<br>Auto Accidents</div>
    </div>
  </section>

  <!-- Business card, front -->
  <section class="piece card-front">
    <div class="lockup" style="left:44px;top:11px;height:17px">
      <span class="square" style="width:17px;height:17px"></span>
      <span class="divider" style="margin:0 3px"></span>
      <span class="wordmark"><span class="small" style="font-size:4px">Law Office of</span><span class="big" style="font-size:8.5px">Nora T. Pask</span></span>
    </div>
    <div class="address" style="left:74px;top:31px;font-size:4.3px">47 W. Orrin Avenue, Suite 315<br>Chicago, IL 60614</div>
    <div class="holder">Nora T. Pask</div>
    <div class="contacts">
      <div><span class="icon"></span>312-555-0148</div>
      <div><span class="icon"></span>773-555-0172</div>
      <div><span class="icon"></span>ntp@norapasklegal.example</div>
      <div><span class="icon"></span>www.norapasklegal.example</div>
    </div>
  </section>

  <!-- Envelope, front -->
  <section class="piece envelope">
    <div class="lockup" style="left:33px;top:42px;height:24px">
      <span class="square" style="width:24px;height:24px"></span>
      <span class="divider"></span>
      <span class="wordmark"><span class="small" style="font-size:6px">Law Office of</span><span class="big" style="font-size:12px">Nora T. Pask</span></span>
    </div>
    <div class="address" style="left:71px;top:71px;font-size:5.8px">47 W. Orrin Avenue, Suite 315<br>Chicago, IL 60614</div>
  </section>

  <!-- Envelope, back with flap -->
  <section class="piece envelope-back">
    <svg width="383" height="56" viewBox="0 0 383 56" aria-hidden="true">
      <polygon points="0,0 383,0 346,55 37,55" fill="var(--flap)"/>
    </svg>
    <div class="lockup reverse" style="left:130px;top:14px;height:26px">
      <span class="square" style="width:26px;height:26px"></span>
      <span class="divider"></span>
      <span class="wordmark"><span class="small" style="font-size:6px">Law Office of</span><span class="big" style="font-size:13px">Nora T. Pask</span></span>
    </div>
  </section>

  <!-- Letterhead -->
  <section class="piece letterhead">
    <div class="lockup" style="left:61px;top:32px;height:24px">
      <span class="square" style="width:24px;height:24px"></span>
      <span class="divider"></span>
      <span class="wordmark"><span class="small" style="font-size:6px">Law Office of</span><span class="big" style="font-size:13px">Nora T. Pask</span></span>
    </div>
    <div class="address" style="left:104px;top:60px;font-size:5.8px">47 W. Orrin Avenue, Suite 315<br>Chicago, IL 60614</div>

    <div class="letter">
      <div class="recipient"><strong>LOREM IPSUM DOLOR</strong><br>sim aciam peridoffrus at ortantis.<br>Fas ipiantulut omnam inatus<br>Marit. Atabunum iu maxim<br>troximant, ta acrit,</div>
      <p>Lorem ipsum dolor sit amet, consectetuer adipiscing elit. Aenean commodo ligula eget dolor. Aenean massa. Cum sociis natoque penatibus et magnis dis parturient montes, nascetur ridiculus mus. Donec quam felis, ultricies nec, pellentesque eu, pretium quis, sem. Nulla consequat massa quis enim. Donec pede justo, fringilla vel, aliquet nec, vulputate eget, arcu. In enim justo, rhoncus ut, imperdiet a, venenatis vitae, justo. Nullam dictum felis eu pede mollis pretium. Integer tincidunt. Cras dapibus. Vivamus elementum semper nisi. Aenean vulputate eleifend tellus. Aenean leo ligula, porttitor eu, consequat vitae, eleifend ac, enim. Aliquam lorem ante, dapibus in, viverra quis, feugiat a, tellus.</p>
      <p>Phasellus viverra nulla ut metus varius laoreet. Quisque rutrum. Aenean imperdiet. Etiam ultricies nisi vel augue. Curabitur ullamcorper ultricies nisi. Nam eget dui. Etiam rhoncus. Maecenas tempus, tellus eget condimentum rhoncus, sem quam semper libero, sit amet adipiscing sem neque sed ipsum. Nam quam nunc, blandit vel, luctus pulvinar, hendrerit id, lorem. Maecenas nec odio et ante tincidunt tempus. Donec vitae sapien ut libero venenatis faucibus. Nullam quis ante. Etiam sit amet orci eget eros faucibus tincidunt.</p>
      <p>Vestibulum purus quam, scelerisque ut, mollis sed, nonummy id, metus. Nullam accumsan lorem in dui. Cras ultricies mi eu turpis hendrerit fringilla. Vestibulum ante ipsum primis in faucibus orci luctus et ultrices posuere cubilia Curae; diet feugiat imperdiet, quis porttitor congue, elit erat euismod orci, ac</p>
      <p class="closing">Idatil namur</p>
    </div>
    <div class="signature" role="img" aria-label="Handwritten signature of the sender"></div>

    <div class="letter-footer">
      <span><span class="contacts"><span class="icon"></span></span>ntp@norapasklegal.example</span>
      <span><span class="contacts"><span class="icon"></span></span>312-555-0148</span>
      <span><span class="contacts"><span class="icon"></span></span>www.norapasklegal.example</span>
    </div>
  </section>

  <!-- Continuation sheet -->
  <section class="piece second-sheet">
    <div class="lockup" style="left:17px;top:22px;height:19px">
      <span class="square" style="width:19px;height:19px"></span>
      <span class="divider"></span>
      <span class="wordmark"><span class="small" style="font-size:4.8px">Law Office of</span><span class="big" style="font-size:10px">Nora T. Pask</span></span>
    </div>
  </section>

  <!-- Folder / practice areas sheet -->
  <section class="piece folder">
    <div class="practice">
      <span>Personal Injury</span>
      <span>Wrongful Death</span>
      <span>Medical Malpractice</span>
      <span>Auto Accidents</span>
    </div>
  </section>

</div>
</body>
</html>
```